Bref créative
TORV stationery
Stationery
Simple
Marco Daniel Fervone Lusse de Telvin
Administrador
Rua das Acácias nº17 Luanda-Angola
marco.telvin@torv-exemplo.com
www.torv-exemplo.com

```html
<!DOCTYPE html>
<html lang="pt">
<head>
<meta charset="utf-8">
<title>TORV stationery</title>
<link href="https://fonts.googleapis.com/css2?family=Open+Sans:wght@400;700;800&display=swap" rel="stylesheet">
<style>
:root{
  --blue:#1d6fb8;
  --blue-light:#4fa3e0;
  --orange:#f39200;
  --ink:#3a3a3a;
  --paper:#ffffff;
  --bg:#e9e6e2;
  --line:#9aa3ad;
  --black:#151515;
}
*{margin:0;padding:0;box-sizing:border-box}
html,body{width:1200px;height:418px;overflow:hidden;background:var(--bg);font-family:"Open Sans",sans-serif;color:var(--ink)}
.canvas{position:relative;width:1200px;height:418px}
.sheet{position:absolute;background:var(--paper);box-shadow:0 1px 4px rgba(0,0,0,.25);overflow:hidden}
.swoosh{position:absolute;display:block}
.brand{position:absolute;display:flex;align-items:center;gap:4px;font-weight:800;color:var(--blue);line-height:1}
.brand-square{background:var(--orange);display:inline-block}
.contact{position:absolute;color:#fff;font-size:4px;line-height:1.35}
.contact.dark{color:var(--ink)}
.fax-title{position:absolute;right:16px;top:66px;font-weight:800;font-size:13px;color:var(--ink)}
.fax-table{position:absolute;left:16px;right:16px;top:86px;border-collapse:collapse;font-size:5px}
.fax-table td{border-bottom:0.6px solid var(--line);height:9px;padding-left:2px}
.fax-table td.label{width:26px;font-weight:700}
.fax-checks{position:absolute;left:16px;right:16px;top:146px;display:flex;justify-content:space-between;font-size:4.5px}
.fax-checks span::before{content:"";display:inline-block;width:4px;height:4px;border:0.6px solid var(--ink);margin-right:2px;vertical-align:middle}
.footer-note{position:absolute;font-size:3.5px;color:var(--ink)}
.flap{position:absolute;left:0;top:0;width:100%;height:100%}
.card-black{background:var(--black)}
.card-black .brand{color:#fff}
</style>
</head>
<body>
<div class="canvas">

  <!-- Fax sheet -->
  <section class="sheet fax" style="left:19px;top:12px;width:271px;height:317px">
    <svg class="swoosh" style="left:0;top:0" width="271" height="46" viewBox="0 0 271 46" preserveAspectRatio="none">
      <path d="M100 0 H271 V40 C220 20 160 18 100 0Z" fill="var(--orange)"/>
      <path d="M110 0 H271 V32 C220 14 165 12 110 0Z" fill="var(--blue)"/>
    </svg>
    <div class="brand" style="left:14px;top:18px;font-size:14px"><span class="brand-square" style="width:10px;height:10px"></span>TORV</div>
    <div class="contact" style="left:190px;top:5px">Marco Daniel Fervone Lusse de Telvin<br>Rua das Acácias nº17 Luanda-Angola<br>marco.telvin@torv-exemplo.com<br>www.torv-exemplo.com</div>
    <div class="fax-title">FAX</div>
    <table class="fax-table">
      <tr><td class="label">To:</td><td></td><td class="label">From:</td><td></td></tr>
      <tr><td class="label">Fax:</td><td></td><td class="label">Pages:</td><td></td></tr>
      <tr><td class="label">Phone:</td><td></td><td class="label">Date:</td><td></td></tr>
      <tr><td class="label">Re:</td><td></td><td class="label">Cc:</td><td></td></tr>
    </table>
    <div class="fax-checks"><span>Urgent</span><span>For Review</span><span>Please Comment</span><span>Please Reply</span><span>Please Recycle</span></div>
  </section>

  <!-- Letterhead -->
  <section class="sheet letterhead" style="left:305px;top:12px;width:271px;height:317px">
    <svg class="swoosh" style="left:0;top:0" width="271" height="46" viewBox="0 0 271 46" preserveAspectRatio="none">
      <path d="M100 0 H271 V40 C220 20 160 18 100 0Z" fill="var(--orange)"/>
      <path d="M110 0 H271 V32 C220 14 165 12 110 0Z" fill="var(--blue)"/>
    </svg>
    <div class="brand" style="left:14px;top:18px;font-size:14px"><span class="brand-square" style="width:10px;height:10px"></span>TORV</div>
    <div class="contact" style="left:190px;top:5px">Marco Daniel Fervone Lusse de Telvin<br>Rua das Acácias nº17 Luanda-Angola<br>marco.telvin@torv-exemplo.com<br>www.torv-exemplo.com</div>
  </section>

  <!-- DL envelope front -->
  <section class="sheet envelope-front" style="left:588px;top:17px;width:281px;height:117px">
    <svg class="swoosh" style="left:0;top:0" width="281" height="50" viewBox="0 0 281 50" preserveAspectRatio="none">
      <defs><linearGradient id="bandA" x1="0" x2="1"><stop offset="0" stop-color="var(--blue)"/><stop offset="1" stop-color="var(--blue-light)"/></linearGradient></defs>
      <path d="M0 0 H281 V30 C180 50 90 48 0 36Z" fill="var(--orange)"/>
      <path d="M0 0 H281 V24 C180 42 90 40 0 30Z" fill="url(#bandA)"/>
    </svg>
    <div class="brand" style="left:12px;top:10px;font-size:12px;color:#fff"><span class="brand-square" style="width:9px;height:9px"></span>TORV</div>
    <div class="contact" style="left:160px;top:6px">Marco Daniel Fervone Lusse de Telvin<br>Rua das Acácias nº17 Luanda-Angola<br>marco.telvin@torv-exemplo.com</div>
  </section>

  <!-- DL envelope back -->
  <section class="sheet envelope-back" style="left:588px;top:144px;width:281px;height:96px">
    <svg class="flap" viewBox="0 0 281 96" preserveAspectRatio="none">
      <path d="M0 0 H281 V22 L150 52 H131 L0 22Z" fill="var(--blue)"/>
      <path d="M0 22 L131 52 H150 L281 22" fill="none" stroke="var(--orange)" stroke-width="1.2"/>
    </svg>
  </section>

  <!-- DL envelope with centred brand -->
  <section class="sheet envelope-plain" style="left:588px;top:252px;width:281px;height:115px">
    <svg class="flap" viewBox="0 0 281 115" preserveAspectRatio="none">
      <path d="M0 0 L131 34 H150 L281 0" fill="none" stroke="#d7d7d7" stroke-width="0.8"/>
    </svg>
    <div class="brand" style="left:124px;top:28px;font-size:8px"><span class="brand-square" style="width:6px;height:6px"></span>TORV</div>
  </section>

  <!-- Business card: contact side -->
  <section class="sheet card card-info" style="left:905px;top:105px;width:90px;height:52px">
    <svg class="swoosh" style="left:0;top:0" width="90" height="52" viewBox="0 0 90 52" preserveAspectRatio="none">
      <path d="M55 0 H90 V52 H70 C78 30 70 12 55 0Z" fill="var(--orange)"/>
      <path d="M60 0 H90 V52 H75 C82 30 76 12 60 0Z" fill="var(--blue)"/>
    </svg>
    <div class="brand" style="left:6px;top:28px;font-size:8px"><span class="brand-square" style="width:6px;height:6px"></span>TORV</div>
    <div class="contact dark" style="left:6px;top:5px;font-size:3px">Marco Daniel Fervone Lusse de Telvin<br>Administrador<br>marco.telvin@torv-exemplo.com</div>
  </section>

  <!-- Business card: logo side -->
  <section class="sheet card card-logo" style="left:905px;top:166px;width:90px;height:52px">
    <div class="brand" style="left:24px;top:19px;font-size:12px"><span class="brand-square" style="width:9px;height:9px"></span>TORV</div>
  </section>

  <!-- Business card: dark variant -->
  <section class="sheet card card-black" style="left:1002px;top:166px;width:90px;height:52px">
    <div class="brand" style="left:24px;top:19px;font-size:12px"><span class="brand-square" style="width:9px;height:9px"></span>TORV</div>
  </section>

  <!-- C5 envelope -->
  <section class="sheet envelope-c5" style="left:900px;top:269px;width:293px;height:122px">
    <svg class="swoosh" style="left:0;top:0" width="293" height="40" viewBox="0 0 293 40" preserveAspectRatio="none">
      <path d="M120 0 H293 V34 C240 16 180 12 120 0Z" fill="var(--orange)"/>
      <path d="M132 0 H293 V26 C240 10 185 8 132 0Z" fill="var(--blue)"/>
    </svg>
    <div class="brand" style="left:14px;top:14px;font-size:16px"><span class="brand-square" style="width:12px;height:12px"></span>TORV</div>
    <div class="footer-note" style="left:14px;bottom:8px">Rua das Acácias nº17 Luanda-Angola</div>
  </section>

</div>
</body>
</html>
```